Business Card Design Project

business cards to match the logo design reference 1970674
specific details to be provided asap - message to follow
hello - thank you for the logo design (reference 1970674) which we are very happy with. In terms of business cards you presented a couple of options ie blue front/white back and then the reverse. Can we start with the white front version but change the text details to black font?
Actual details are as follows;
Dorian Plimsoll
Managing Director
e dorianplimsoll@kestrowe.com.au
t +61 2 5550 1937
m +61 400 555 219
Suite 712, Level 7, 48 Thornbury Rd
Sydney, NSW 2000, Australia
www.kestrowe.com.au

```html
<!DOCTYPE html>
<html lang="en">
<head>
<meta charset="utf-8">
<title>Kestrowe Business Card</title>
<link rel="stylesheet" href="https://fonts.googleapis.com/css2?family=Open+Sans:wght@400;600;700&display=swap">
<style>
  :root {
    --stage: #2b2b2b;
    --card-white: #ffffff;
    --card-white-edge: #e9ecef;
    --blue-light: #3aa9e0;
    --blue-mid: #1f8fd0;
    --blue-deep: #0f6fae;
    --wordmark-grey: #555a5e;
    --text-black: #111111;
    --faint-blue: rgba(31, 143, 208, 0.08);
  }
  * { box-sizing: border-box; margin: 0; padding: 0; }
  html, body {
    width: 1200px;
    height: 900px;
    overflow: hidden;
  }
  body {
    background: var(--stage);
    font-family: "Open Sans", Arial, sans-serif;
    position: relative;
  }
  .card {
    position: absolute;
    left: 280px;
    width: 640px;
    height: 390px;
    border-radius: 26px;
    overflow: hidden;
  }
  .card-back {
    top: 40px;
    background: linear-gradient(160deg, var(--blue-light) 0%, var(--blue-mid) 55%, var(--blue-deep) 100%);
  }
  .card-back .back-glow {
    position: absolute;
    inset: 0;
    background: radial-gradient(ellipse at 30% 60%, rgba(255,255,255,0.10), rgba(255,255,255,0) 60%);
  }
  .card-back .wordmark {
    position: absolute;
    right: 48px;
    bottom: 44px;
    font-weight: 600;
    font-size: 40px;
    letter-spacing: 1px;
    color: #ffffff;
  }
  .card-front {
    top: 470px;
    background: linear-gradient(180deg, var(--card-white) 0%, var(--card-white-edge) 100%);
  }
  .card-front .front-glow {
    position: absolute;
    left: 0; top: 0;
    width: 62%; height: 100%;
    background: radial-gradient(ellipse at 40% 45%, var(--faint-blue), rgba(255,255,255,0) 70%);
  }
  .logo-lockup {
    position: absolute;
    left: 40px;
    bottom: 44px;
    display: flex;
    align-items: center;
    gap: 16px;
  }
  .logo-dot {
    width: 54px;
    height: 54px;
    border-radius: 50%;
    background: var(--blue-mid);
  }
  .logo-lockup .wordmark {
    font-weight: 600;
    font-size: 46px;
    letter-spacing: 1px;
    color: var(--wordmark-grey);
  }
  .contact-block {
    position: absolute;
    left: 340px;
    top: 44px;
    color: var(--text-black);
    white-space: nowrap;
  }
  .person-name {
    font-weight: 700;
    font-size: 20px;
  }
  .person-role {
    font-size: 14px;
    margin: 2px 0 0 14px;
  }
  .contact-lines {
    list-style: none;
    margin: 30px 0 0 36px;
    font-size: 13px;
    line-height: 21px;
  }
  .contact-lines .label {
    display: inline-block;
    width: 18px;
    font-weight: 600;
  }
  .address {
    margin: 30px 0 0 54px;
    font-size: 13px;
    line-height: 21px;
    font-style: normal;
  }
  .address .website {
    font-weight: 600;
  }
</style>
</head>
<body>
  <section class="card card-back" aria-label="Card back">
    <div class="back-glow"></div>
    <div class="wordmark">Kestrowe</div>
  </section>

  <section class="card card-front" aria-label="Card front">
    <div class="front-glow"></div>
    <div class="logo-lockup">
      <span class="logo-dot"></span>
      <span class="wordmark">Kestrowe</span>
    </div>
    <div class="contact-block">
      <p class="person-name">Dorian Plimsoll</p>
      <p class="person-role">Managing Director</p>
      <ul class="contact-lines">
        <li><span class="label">t</span>+61 2 5550 1937</li>
        <li><span class="label">m</span>+61 400 555 219</li>
        <li><span class="label">e</span>dorianplimsoll@kestrowe.com.au</li>
      </ul>
      <address class="address">
        Suite 712, Level 7, 48 Thornbury Rd<br>
        Sydney, NSW 2000, Australia<br>
        <span class="website">www.kestrowe.com.au</span>
      </address>
    </div>
  </section>
</body>
</html>
```